KOVA WIRING PTE LTD
KOVA WIRING NAME CARD
Project: KOVA WIRING PTE LTD
KOVA WIRING PTE LTD - Engineering
Creative Brief
Professional
Deren Whitcombe
Manager
57 Tannery Lane #03-22 Silverbrook Industrial Complex Singapore 347912
derenkovawiring@mailbox-example.net
Reg No. 198733502K
https://www.filevault-example.net/share/7qe2kx9/ZTRmPwq4HnLc?dl=0 Pleas find folder for the logo design A.I. file. Thanks Client love the 3 colour in the logo design for FengShui purposes.
harlowbek harlowbek
Hi my client like your design #218, Can you give the stationary set for #218. We try to finalize by tomorrow. Thanks

```html
<!DOCTYPE html>
<html lang="en">
<head>
<meta charset="UTF-8">
<title>KOVA WIRING – Name Card</title>
<link rel="stylesheet" href="https://fonts.googleapis.com/css2?family=Montserrat:wght@400;500;600&display=swap">
<style>
  :root {
    --page-bg: #d9d6d2;
    --card-frost: #eceef0;
    --card-frost-edge: #dfe2e5;
    --band-black: #0e0e0e;
    --ink-dark: #1c1c1c;
    --ink-grey: #6a6d70;
    --ink-white: #ffffff;
    --ink-soft: #c9c9c9;
    --rule-grey: #b9bcbf;
    --mark-green: #2f9e4a;
  }
  * { box-sizing: border-box; margin: 0; padding: 0; }
  html, body {
    width: 1200px; height: 770px; overflow: hidden;
    background: var(--page-bg);
    font-family: "Montserrat", sans-serif;
  }
  .canvas {
    width: 1200px; height: 770px;
    display: flex; align-items: center; justify-content: center;
  }
  .name-card {
    position: relative;
    width: 1000px; height: 560px;
    border-radius: 22px;
    background: linear-gradient(180deg, var(--card-frost) 0%, var(--card-frost-edge) 100%);
    box-shadow: 0 18px 40px rgba(0,0,0,0.18);
    overflow: hidden;
  }
  .brand {
    position: absolute; top: 105px; left: 0; right: 0;
    display: flex; align-items: center; justify-content: center; gap: 22px;
  }
  .brand-square {
    width: 62px; height: 62px; background: var(--mark-green);
  }
  .brand-name {
    font-weight: 600; font-size: 50px; letter-spacing: 3px;
    color: var(--ink-dark);
  }
  .contact-band {
    position: absolute; left: 0; right: 0; top: 268px; height: 200px;
    background: var(--band-black);
  }
  .band-notch {
    position: absolute; left: 178px; top: 250px;
    width: 0; height: 0;
    border-left: 18px solid transparent;
    border-right: 18px solid transparent;
    border-bottom: 18px solid var(--band-black);
  }
  .person {
    position: absolute; left: 60px; top: 60px; width: 360px; text-align: center;
  }
  .person-name {
    font-size: 30px; font-weight: 500; letter-spacing: 1px; color: var(--ink-white);
    text-transform: uppercase;
  }
  .person-title {
    margin-top: 8px; font-size: 20px; color: var(--ink-soft);
  }
  .band-divider {
    position: absolute; left: 470px; top: 28px; width: 2px; height: 144px;
    background: var(--ink-soft);
  }
  .contact-list {
    position: absolute; left: 505px; top: 26px; list-style: none;
  }
  .contact-list li {
    display: flex; align-items: center; gap: 14px;
    height: 30px; margin-bottom: 6px;
    font-size: 16px; color: var(--ink-white);
  }
  .contact-list li.address { font-size: 13px; line-height: 1.25; height: 36px; }
  .contact-icon { width: 22px; height: 22px; flex: none; }
  .website-row {
    position: absolute; left: 0; right: 0; top: 490px;
    display: flex; align-items: center; justify-content: center; gap: 18px;
  }
  .website-rule { width: 150px; height: 2px; background: var(--rule-grey); }
  .website {
    font-size: 18px; letter-spacing: 1.5px; color: var(--ink-grey);
  }
</style>
</head>
<body>
<main class="canvas">
  <section class="name-card" aria-label="KOVA WIRING name card">
    <div class="brand">
      <span class="brand-square"></span>
      <span class="brand-name">KOVA WIRING</span>
    </div>

    <div class="band-notch"></div>
    <div class="contact-band">
      <div class="person">
        <p class="person-name">Deren Whitcombe</p>
        <p class="person-title">Manager</p>
      </div>
      <div class="band-divider"></div>
      <ul class="contact-list">
        <li>
          <svg class="contact-icon" viewBox="0 0 22 22"><circle cx="11" cy="11" r="11" fill="#fff"/><path d="M7.5 6h2l1 2.6-1.3 1a6 6 0 0 0 3.2 3.2l1-1.3 2.6 1v2a1 1 0 0 1-1 1A9 9 0 0 1 6.5 7a1 1 0 0 1 1-1z" fill="#0e0e0e"/></svg>
          065 118 2040
        </li>
        <li>
          <svg class="contact-icon" viewBox="0 0 22 22"><circle cx="11" cy="11" r="11" fill="#fff"/><path d="M7.5 6h2l1 2.6-1.3 1a6 6 0 0 0 3.2 3.2l1-1.3 2.6 1v2a1 1 0 0 1-1 1A9 9 0 0 1 6.5 7a1 1 0 0 1 1-1z" fill="#0e0e0e"/></svg>
          065 118 2041
        </li>
        <li>
          <svg class="contact-icon" viewBox="0 0 22 22"><circle cx="11" cy="11" r="11" fill="#fff"/><rect x="5.5" y="7" width="11" height="8" rx="1" fill="#0e0e0e"/><path d="M6 7.6l5 3.9 5-3.9" stroke="#fff" stroke-width="1" fill="none"/></svg>
          derenkovawiring@mailbox-example.net
        </li>
        <li class="address">
          <svg class="contact-icon" viewBox="0 0 22 22"><circle cx="11" cy="11" r="11" fill="#fff"/><path d="M11 4.5a4.3 4.3 0 0 0-4.3 4.3c0 3.2 4.3 8.4 4.3 8.4s4.3-5.2 4.3-8.4A4.3 4.3 0 0 0 11 4.5z" fill="#0e0e0e"/><circle cx="11" cy="8.8" r="1.6" fill="#fff"/></svg>
          <span>57 Tannery Lane #03-22 Silverbrook Industrial Complex<br>Singapore 347912</span>
        </li>
      </ul>
    </div>

    <div class="website-row">
      <span class="website-rule"></span>
      <span class="website">www.kovawiring-example.net</span>
      <span class="website-rule"></span>
    </div>
  </section>
</main>
</body>
</html>
```